Electrician Letterhead Design BLR

We need some letterhead for our bills and other papers.
Customer address is on the right side (Swiss format)
A4 format

Design should also be applicable on Cards

Target Market(s)

Private Customers, Small Business

Industry/Entity Type

Electrician

Other font styles liked:
• incised 901

Colors
00AB8E
00BBA5
67D7C9
C6EFE9
E9F9F6

```html
<!DOCTYPE html>
<html lang="en">
<head>
<meta charset="utf-8">
<title>BLR Letterhead</title>
<link href="https://fonts.googleapis.com/css2?family=Montserrat:wght@400;500;800&family=Great+Vibes&display=swap" rel="stylesheet">
<style>
  :root{
    --teal:#00A08A;
    --teal-bright:#00BBA5;
    --mint:#67D7C9;
    --ice:#E9F9F6;
    --paper:#FFFFFF;
    --text:#5A5A5A;
    --ink:#1A1A1A;
  }
  *{margin:0;padding:0;box-sizing:border-box}
  html,body{width:1200px;height:1200px;overflow:hidden}
  body{background:var(--ice);font-family:'Montserrat',sans-serif;color:var(--text)}
  .letterhead{position:absolute;left:190px;top:20px;width:820px;height:1160px;background:var(--paper);box-shadow:0 4px 18px rgba(0,80,70,.12)}
  .brand{position:absolute;right:100px;top:62px;display:flex;align-items:center;gap:14px}
  .brand-mark{width:26px;height:26px;background:var(--teal)}
  .brand-name{font-family:'Montserrat',sans-serif;font-weight:800;font-size:112px;line-height:1;color:var(--teal);letter-spacing:2px}
  .recipient{position:absolute;right:100px;top:228px;text-align:right;font-size:14px;line-height:19.3px;font-style:normal}
  .salutation{position:absolute;left:97px;top:340px;font-size:14px}
  .body{position:absolute;left:99px;top:372px;width:621px;font-size:14.2px;line-height:18px;text-align:justify;hyphens:auto}
  .body p{text-indent:83px;margin-bottom:18px}
  .closing{position:absolute;left:99px;top:872px;font-size:14px;line-height:19.3px}
  .signature{position:absolute;left:99px;top:926px;width:140px;white-space:nowrap;border-bottom:1.5px solid var(--text);font-family:'Great Vibes',cursive;font-size:30px;line-height:40px;color:var(--text)}
  .signer{position:absolute;left:99px;top:982px;font-size:14px;line-height:19.3px}
  .contact{position:absolute;right:97px;top:964px;display:flex;gap:7px}
  .contact-list{list-style:none;text-align:right;font-size:14px;font-weight:500;color:var(--ink);padding-top:6px}
  .contact-list li{height:24.7px;line-height:24.7px;white-space:nowrap}
  .icon-bar{width:22px;height:135px;background:var(--teal);border-radius:3px;display:flex;flex-direction:column;align-items:center;padding-top:8px}
  .icon-bar svg{width:14px;height:14px;margin-bottom:10.7px;fill:#fff}
</style>
</head>
<body>
<main class="letterhead">
  <header class="brand">
    <span class="brand-mark"></span>
    <span class="brand-name">BLR</span>
  </header>

  <address class="recipient">
    To<br>Lena Hofer<br>HR Manager<br>Your company<br>Address<br>Date
  </address>

  <p class="salutation">Dear Sir</p>

  <section class="body">
    <p>Lorem ipsum dolor sit amet, consectetur adipiscing elit. Pellentesque facilisis sollicitudin ante. Pellentesque habitant morbi tristique senectus et netus et malesuada fames ac turpis egestas. Nunc feugiat tortor nunc, quis feugiat lectus mattis sit amet. Nunc urna velit, convallis scelerisque odio non, pulvinar tincidunt massa. Proin pulvinar lacus at ex auctor consequat. Maecenas eleifend tempus posuere. Aliquam non pretium metus. Mauris nibh velit, molestie et lorem quis, hendrerit lacinia nunc. Donec in dignissim augue. Curabitur vitae erat nisi. Vestibulum ante ipsum primis in faucibus orci luctus et ultrices posuere cubilia Curae; Aliquam blandit magna ac augue placerat luctus. Ut et vehicula odio. Vivamus tincidunt diam diam, sed facilisis lectus pretium quis. Sed vel mi accumsan, luctus metus vel, congue ex.</p>
    <p>Curabitur non tristique tellus. Nam maximus fermentum metus sit amet luctus. Cras semper nunc id urna lacinia, in interdum quam mollis. Mauris sit amet eros vel lorem facilisis semper non ac nunc. Curabitur ornare suscipit lacus. Duis sit amet lectus vitae nulla consectetur ullamcorper vitae id urna. Sed dictum at lectus eget vehicula. Phasellus non lacinia nunc. Mauris ex tortor, ultricies luctus lectus egestas, gravida ornare elit. In tempor libero non ullamcorper sagittis. Phasellus interdum pulvinar lacus vel sodales. Praesent nec velit bibendum, accumsan magna non, molestie tortor. Nam a est at arcu porta auctor quis id tortor.</p>
    <p>Curabitur non tristique tellus. Nam maximus fermentum metus sit amet luctus. Cras semper nunc id urna lacinia, in interdum quam mollis. Mauris sit amet eros vel lorem facilisis semper non ac nunc. Curabitur ornare suscipit lacus. Duis sit amet lectus vitae nulla consectetur ullamcorper vitae id urna. Sed dictum at lectus eget vehicula. Phasellus non lacinia nunc. Mauris ex tortor, ultricies luctus lectus egestas.</p>
  </section>

  <p class="closing">Thank you so much<br>Best Regarding</p>
  <div class="signature">Lena Hofer</div>
  <p class="signer">Lena Hofer<br>HR Manager</p>

  <footer class="contact">
    <ul class="contact-list">
      <li>+000 12345 6789</li>
      <li>+000 12345 6789</li>
      <li>yourname@email.com</li>
      <li>www.yourname.com</li>
      <li>Street Address Here, Country, Zip cord.</li>
    </ul>
    <div class="icon-bar">
      <svg viewBox="0 0 16 16"><path d="M4 0h8a1 1 0 0 1 1 1v14a1 1 0 0 1-1 1H4a1 1 0 0 1-1-1V1a1 1 0 0 1 1-1zm1 2v10h6V2zm3 11a1 1 0 1 0 0 2 1 1 0 0 0 0-2z"/></svg>
      <svg viewBox="0 0 16 16"><path d="M3.6 1l2.6 2.8-1.5 2.3c.9 2 2.3 3.4 4.3 4.3l2.3-1.5L14 11.5 12.6 15C6.5 14.6 1.4 9.5 1 3.4z"/></svg>
      <svg viewBox="0 0 16 16"><path d="M0 3h16v10H0zm1.5 1.2v.4L8 9l6.5-4.4v-.4zM1 12h14V6L8 10.5 1 6z"/></svg>
      <svg viewBox="0 0 16 16"><path d="M3 0l10 9-4.3.4 2.6 5.3-2 1-2.6-5.4L3 13z"/></svg>
      <svg viewBox="0 0 16 16"><path d="M8 0a5.5 5.5 0 0 1 5.5 5.5C13.5 10 8 16 8 16S2.5 10 2.5 5.5A5.5 5.5 0 0 1 8 0zm0 3a2.5 2.5 0 1 0 0 5 2.5 2.5 0 0 0 0-5z"/></svg>
    </div>
  </footer>
</main>
</body>
</html>
```